Cedar Hall businesscard

We changed our name and logo, now we need new business cards.
3-4/72 Marlow Street Kelsey Park 2999
www.cedarhall-example.org.au
info@cedarhall-example.org.au
Lorna-Jean Whitcombe
Senior Pastor
ph: 02 95874210

```html
<!DOCTYPE html>
<html lang="en">
<head>
<meta charset="utf-8">
<title>Cedar Hall – Business Card</title>
<link href="https://fonts.googleapis.com/css2?family=Lato:wght@400;700&display=swap" rel="stylesheet">
<style>
  :root {
    --page-bg: #ecebe8;
    --card-white: #ffffff;
    --brand-red: #e52a35;
    --edge-grey: #9aa3ab;
    --text-grey: #8c9298;
    --mark-grey: #6f767d;
    --icon-grey: #a7adb3;
  }
  * { margin: 0; padding: 0; box-sizing: border-box; }
  html, body {
    width: 1200px; height: 1022px; overflow: hidden;
    background: var(--page-bg);
    font-family: "Lato", Arial, sans-serif;
  }
  .card {
    position: absolute; left: 150px; top: 251px;
    width: 900px; height: 520px;
    background: var(--card-white);
    box-shadow: 0 10px 30px rgba(0,0,0,.15);
    overflow: hidden;
  }
  .card-shapes { position: absolute; inset: 0; }
  .holder {
    position: absolute; left: 50px; top: 205px;
    text-align: right; width: 300px;
  }
  .holder-name {
    color: var(--brand-red); font-weight: 700; font-size: 26px; letter-spacing: .2px;
  }
  .holder-role {
    color: var(--text-grey); font-weight: 400; font-size: 16px; margin-top: 4px;
  }
  .brand {
    position: absolute; left: 378px; top: 236px;
    width: 150px;
    display: flex; flex-direction: column; align-items: center; gap: 8px;
  }
  .brand-dot {
    width: 14px; height: 14px; border-radius: 50%;
    background: var(--icon-grey);
  }
  .brand-name {
    color: var(--mark-grey); font-weight: 400; font-size: 20px; letter-spacing: .5px;
    white-space: nowrap;
  }
  .contacts {
    position: absolute; left: 560px; top: 192px;
    list-style: none;
  }
  .contact {
    display: flex; align-items: center; gap: 10px;
    color: var(--brand-red); font-size: 15.5px; font-weight: 400;
    height: 31px; white-space: nowrap;
  }
  .contact-icon { width: 18px; height: 18px; flex: none; }
</style>
</head>
<body>
  <div class="card">
    <svg class="card-shapes" width="900" height="520" viewBox="0 0 900 520">
      <path d="M0 0 H900 V66 Q500 210 0 132 Z" fill="var(--brand-red)"/>
      <path d="M0 132 Q500 210 900 66" fill="none" stroke="var(--edge-grey)" stroke-width="6"/>
      <path d="M0 392 Q420 318 900 470 V520 H0 Z" fill="var(--brand-red)"/>
      <path d="M0 392 Q420 318 900 470" fill="none" stroke="var(--edge-grey)" stroke-width="6"/>
    </svg>

    <div class="holder">
      <p class="holder-name">Lorna-Jean Whitcombe</p>
      <p class="holder-role">Senior Pastor</p>
    </div>

    <div class="brand">
      <span class="brand-dot"></span>
      <span class="brand-name">Cedar Hall</span>
    </div>

    <ul class="contacts">
      <li class="contact">
        <svg class="contact-icon" viewBox="0 0 18 18"><rect width="18" height="18" rx="2" fill="var(--icon-grey)"/><path d="M5 4 L7.5 4 L8.3 6.8 L7 7.8 Q8 10 10.2 11 L11.2 9.7 L14 10.5 L14 13 Q8 14 5 8 Z" fill="#fff"/></svg>
        02 95874210
      </li>
      <li class="contact">
        <svg class="contact-icon" viewBox="0 0 18 18"><rect width="18" height="18" rx="2" fill="var(--icon-grey)"/><circle cx="9" cy="9" r="5" fill="none" stroke="#fff" stroke-width="1.3"/><path d="M4 9 H14 M9 4 Q6 9 9 14 M9 4 Q12 9 9 14" fill="none" stroke="#fff" stroke-width="1"/></svg>
        www.cedarhall-example.org.au
      </li>
      <li class="contact">
        <svg class="contact-icon" viewBox="0 0 18 18"><rect width="18" height="18" rx="2" fill="var(--icon-grey)"/><rect x="4" y="5.5" width="10" height="7" fill="none" stroke="#fff" stroke-width="1.3"/><path d="M4 5.5 L9 10 L14 5.5" fill="none" stroke="#fff" stroke-width="1.3"/></svg>
        info@cedarhall-example.org.au
      </li>
      <li class="contact">
        <svg class="contact-icon" viewBox="0 0 18 18"><rect width="18" height="18" rx="2" fill="var(--icon-grey)"/><path d="M9 3.5 A3.8 3.8 0 0 1 12.8 7.3 Q12.8 10 9 14.5 Q5.2 10 5.2 7.3 A3.8 3.8 0 0 1 9 3.5 Z" fill="#fff"/><circle cx="9" cy="7.3" r="1.4" fill="var(--icon-grey)"/></svg>
        3-4/72 Marlow Street Kelsey Park 2999
      </li>
    </ul>
  </div>
</body>
</html>
```